Hearthside Pots: A Patient Palate's Companion

Hi, I had a book cover designed on this site, but I want to modify the cover and change the colours. I want to keep the slow cooker and the ingredients on the cover, but I want to simplify it a bit. And, I am open to other ideas. I have attached below a book cover idea I like and I like the colors as well. I want it to be called Hearthside Pots, with the language on the right corner: "Curated For Nearly Effortless Meals That Are Greater Than The Sum Of Their Ingredients" I like the circles idea and my name as the author on the curve.

Target Market(s)

Home Cooks

Colors
00AB8E
00BBA5
67D7C9
C6EFE9
E9F9F6
F0912C
F2A743
F7CA91
FBE8D2
FDF5EE
E54698
E96AAD
F1A4CE
F9D9EA
FCEFF6
6B429C
8869AF
B7A5CE
E3DAEB
F3F0F8

Requirements
Must have
• Please use the colors on the Marigold Table Recipe Book and I like the design, but I do not want it identical. I like the author name (Harold P. Quimby) on the side of the circle on the upper right side of the cover.
Nice to have
• I like the large words "Hearthside Pots"

```html
<!DOCTYPE html>
<html lang="en">
<head>
<meta charset="utf-8">
<title>Hearthside Pots – Book Cover</title>
<link rel="stylesheet" href="https://fonts.googleapis.com/css2?family=Libre+Caslon+Text&family=Montserrat:wght@400;700&display=swap">
<style>
  :root {
    --marigold: #FBAE30;
    --forest: #034E47;
    --teal: #2E6A64;
    --page: #FFFFFF;
  }
  html, body {
    margin: 0;
    width: 1200px;
    height: 1200px;
    overflow: hidden;
    background: var(--page);
  }
  .cover {
    position: absolute;
    left: 231px;
    top: 141px;
    width: 746px;
    height: 926px;
    display: block;
  }
  .bg-marigold { fill: var(--marigold); }
  .bg-teal { fill: var(--teal); }
  .bg-forest { fill: var(--forest); }
  .title {
    font-family: "Libre Caslon Text", serif;
    font-size: 150px;
    fill: var(--marigold);
  }
  .tagline {
    font-family: "Montserrat", sans-serif;
    font-weight: 400;
    font-size: 33px;
    letter-spacing: 1px;
    fill: var(--marigold);
  }
  .author {
    font-family: "Montserrat", sans-serif;
    font-weight: 700;
    font-size: 36px;
    fill: var(--forest);
  }
  .ingredients { isolation: isolate; }
  .ingredient { mix-blend-mode: multiply; }
</style>
</head>
<body>
<svg class="cover" viewBox="0 0 1193 1482" xmlns="http://www.w3.org/2000/svg" aria-label="Hearthside Pots book cover">
  <defs>
    <clipPath id="cover-clip"><rect width="1193" height="1482"/></clipPath>
    <linearGradient id="grad-lilac" x1="0.2" y1="0" x2="0.8" y2="1">
      <stop offset="0" stop-color="#7C9AD6"/>
      <stop offset="0.55" stop-color="#B7A9CF"/>
      <stop offset="1" stop-color="#F4DDE3"/>
    </linearGradient>
    <linearGradient id="grad-pink" x1="0" y1="0" x2="0" y2="1">
      <stop offset="0" stop-color="#EC6778"/>
      <stop offset="0.6" stop-color="#EE7E86"/>
      <stop offset="1" stop-color="#F1A1A6"/>
    </linearGradient>
    <linearGradient id="grad-orange" x1="0" y1="0" x2="0" y2="1">
      <stop offset="0" stop-color="#FF5E10"/>
      <stop offset="0.45" stop-color="#FB7A45"/>
      <stop offset="1" stop-color="#F7908F"/>
    </linearGradient>
    <linearGradient id="grad-blue" x1="0" y1="0" x2="0" y2="1">
      <stop offset="0" stop-color="#3A5AA3"/>
      <stop offset="0.6" stop-color="#5F5F9C"/>
      <stop offset="1" stop-color="#EBC3CF"/>
    </linearGradient>
    <path id="author-curve" d="M150 372 Q 270 180 430 50"/>
  </defs>

  <g clip-path="url(#cover-clip)">
    <rect class="bg-marigold" width="1193" height="1482"/>
    <path class="bg-teal" d="M565 0 C 150 240, -120 800, 240 1482 L1193 1482 L1193 0 Z"/>
    <path class="bg-forest" d="M565 0 Q 420 100 297 230 C 400 650, 800 950, 1193 1035 L1193 0 Z"/>

    <g class="ingredients" role="img" aria-label="Watercolour circles each holding a cooking ingredient or kitchen tool silhouette: chilli, aubergine, cleaver and bell pepper">
      <circle class="ingredient" cx="136" cy="549" r="193" fill="url(#grad-lilac)"/>
      <circle class="ingredient" cx="273" cy="826" r="243" fill="url(#grad-pink)"/>
      <circle class="ingredient" cx="577" cy="1144" r="300" fill="url(#grad-orange)"/>
      <circle class="ingredient" cx="1031" cy="1380" r="342" fill="url(#grad-blue)"/>
    </g>
  </g>

  <text class="author"><textPath href="#author-curve">Harold P. Quimby</textPath></text>

  <text class="title" x="450" y="287" textLength="700" lengthAdjust="spacingAndGlyphs">Hearthside</text>
  <text class="title" x="450" y="472">Pots</text>

  <text class="tagline" x="708" y="568">Curated For Nearly</text>
  <text class="tagline" x="708" y="618">Effortless Meals That Are</text>
  <text class="tagline" x="708" y="668">Greater Than The Sum</text>
  <text class="tagline" x="708" y="718">Of Their Ingredients</text>
</svg>
</body>
</html>
```